We have developed a fully functional App called Harborwink. However, it requires a nicer GUI. You can see screenshots of our App on www.harborwink-example.com under "Tutorial". For those of you with Android, you can also install it. When you go to Harborwink-example.com, your phone will automatically redirect you to download. From there, you'll get a better idea of what our App looks like and how your design can make it way better. Please note we expect a design idea for most screens (there's about 8 screens) but do just one screen first and if you win, you can do the other 8 after.

Target Market(s)

People looking for dating / flirting

Industry/Entity Type

Android

Requirements
Must have
• sleek looking

```html
<!DOCTYPE html>
<html lang="en">
<head>
<meta charset="utf-8">
<title>Harborwink – Profile Settings</title>
<link href="https://fonts.googleapis.com/css2?family=Source+Sans+3:wght@400;600&display=swap" rel="stylesheet">
<style>
  :root {
    --stage: #c6b6c1;
    --status-bg: #0d0d0d;
    --status-blue: #33b5e5;
    --header-bg: #efe1ea;
    --content-bg: #ecdbe6;
    --magenta: #b0237f;
    --magenta-dark: #96156a;
    --tab-dim: #7a1a5a;
    --label: #8c7884;
    --field-text: #a8919f;
    --field-border: #d7c3d0;
    --tick: #1f9dbf;
    --teal-top: #3fb6d3;
    --teal-bottom: #1798b7;
    --teal-line: #6ccbe1;
    --white: #ffffff;
  }
  * { box-sizing: border-box; margin: 0; padding: 0; }
  html, body {
    width: 1024px; height: 1200px; overflow: hidden;
    background: var(--stage);
    font-family: "Source Sans 3", sans-serif;
  }
  .screen {
    position: absolute; left: 153px; top: 2px;
    width: 664px; height: 1108px;
    transform: scale(1.08); transform-origin: top left;
    background: var(--content-bg);
    overflow: hidden;
  }
  .status-bar {
    position: absolute; left: 0; top: 0; width: 100%; height: 38px;
    background: var(--status-bg);
    display: flex; align-items: center; justify-content: flex-end;
    gap: 10px; padding-right: 14px;
    color: var(--status-blue); font-size: 26px;
  }
  .status-bar svg { display: block; }
  .app-header {
    position: absolute; left: 0; top: 38px; width: 100%; height: 168px;
    background: radial-gradient(ellipse 240px 120px at 50% 40%, #ffffff 0%, var(--header-bg) 100%);
    display: flex; align-items: center; justify-content: center; gap: 14px;
  }
  .brand-dot { width: 46px; height: 46px; border-radius: 50%; background: var(--magenta); }
  .brand-name { font-size: 52px; font-weight: 600; color: #6d6b72; letter-spacing: 0.5px; }
  .tabs {
    position: absolute; left: 0; top: 206px; width: 100%; height: 74px;
    display: flex;
    background: linear-gradient(180deg, #c02e8e 0%, var(--magenta-dark) 100%);
  }
  .tab {
    flex: 1; display: flex; align-items: center; justify-content: center;
    font-size: 26px; font-weight: 600;
  }
  .tab--inactive { color: var(--tab-dim); border-right: 1px solid #cf5aa6; }
  .tab--active { color: var(--white); }
  .form { position: absolute; left: 37px; top: 280px; width: 593px; }
  .field-label {
    position: absolute; font-size: 23px; color: var(--label);
  }
  .input {
    position: absolute; height: 70px; background: var(--white);
    border: 2px solid var(--field-border); border-radius: 3px;
    display: flex; align-items: center; padding-left: 24px;
    font-size: 23px; color: var(--field-text);
  }
  .input .tick { position: absolute; right: 20px; top: 24px; }
  .select-btn {
    position: absolute; right: -2px; top: -2px; bottom: -2px; width: 39px;
    background: var(--magenta); border-radius: 0 3px 3px 0;
    display: flex; align-items: center; justify-content: center;
  }
  .bottom-nav {
    position: absolute; left: 0; top: 1000px; width: 100%; height: 108px;
    background: linear-gradient(180deg, var(--teal-top) 0%, var(--teal-bottom) 100%);
    display: flex;
  }
  .nav-item {
    display: flex; flex-direction: column; align-items: center; justify-content: center;
    gap: 4px; color: var(--white); font-size: 19px; font-weight: 600;
  }
  .nav-item + .nav-item { border-left: 1px solid var(--teal-line); }
</style>
</head>
<body>
<main class="screen">
  <div class="status-bar">
    <svg width="26" height="26" viewBox="0 0 26 26"><path d="M5 9h4l6-5v18l-6-5H5z" fill="#9a9a9a"/><path d="M3 23L23 3" stroke="#9a9a9a" stroke-width="2"/></svg>
    <svg width="30" height="26" viewBox="0 0 30 26"><text x="0" y="10" font-size="10" fill="#bbb" font-family="sans-serif">H</text><path d="M4 26L28 2v24z" fill="var(--status-blue)"/></svg>
    <svg width="16" height="26" viewBox="0 0 16 26"><rect x="5" y="1" width="6" height="3" fill="var(--status-blue)"/><rect x="1" y="4" width="14" height="21" fill="var(--status-blue)"/></svg>
    <span>13:37</span>
  </div>

  <header class="app-header">
    <span class="brand-dot"></span>
    <span class="brand-name">Harborwink</span>
  </header>

  <nav class="tabs">
    <div class="tab tab--inactive">Profile</div>
    <div class="tab tab--active">Security</div>
  </nav>

  <section class="form">
    <label class="field-label" style="left:2px; top:38px;">Your Name</label>
    <div class="input" style="left:0; top:85px; width:593px;">Lena Marsh
      <svg class="tick" width="22" height="18" viewBox="0 0 22 18"><path d="M2 9l6 6L20 3" stroke="var(--tick)" stroke-width="4" fill="none"/></svg>
    </div>

    <label class="field-label" style="left:2px; top:188px;">Email</label>
    <div class="input" style="left:0; top:235px; width:593px;">Sunnyday_42@example.com
      <svg class="tick" width="22" height="18" viewBox="0 0 22 18"><path d="M2 9l6 6L20 3" stroke="var(--tick)" stroke-width="4" fill="none"/></svg>
    </div>

    <label class="field-label" style="left:2px; top:339px;">Age</label>
    <label class="field-label" style="left:160px; top:339px;">Height</label>
    <label class="field-label" style="left:394px; top:339px;">Sex</label>

    <div class="input" style="left:0; top:388px; width:121px; height:67px; padding-left:20px;">25
      <span class="select-btn"><svg width="16" height="22" viewBox="0 0 16 22"><path d="M8 1l7 8H1zM8 21l7-8H1z" fill="#fff"/></svg></span>
    </div>
    <div class="input" style="left:158px; top:388px; width:200px; height:67px; padding-left:20px;">5’4”
      <span class="select-btn"><svg width="16" height="22" viewBox="0 0 16 22"><path d="M8 1l7 8H1zM8 21l7-8H1z" fill="#fff"/></svg></span>
    </div>
    <div class="input" style="left:393px; top:388px; width:200px; height:67px; padding-left:20px;">F-Straight
      <span class="select-btn"><svg width="16" height="22" viewBox="0 0 16 22"><path d="M8 1l7 8H1zM8 21l7-8H1z" fill="#fff"/></svg></span>
    </div>

    <label class="field-label" style="left:2px; top:490px;">Discovery</label>
    <div class="input" style="left:0; top:538px; width:593px; height:69px;">Local
      <span class="select-btn"><svg width="16" height="22" viewBox="0 0 16 22"><path d="M8 1l7 8H1zM8 21l7-8H1z" fill="#fff"/></svg></span>
    </div>
  </section>

  <footer class="bottom-nav">
    <div class="nav-item" style="width:225px;">
      <svg width="42" height="40" viewBox="0 0 42 40"><path d="M21 2L2 19h6v19h26V19h6z" fill="#fff"/><rect x="17" y="25" width="8" height="13" fill="var(--teal-bottom)"/></svg>
      <span>Home</span>
    </div>
    <div class="nav-item" style="width:219px;">
      <svg width="54" height="44" viewBox="0 0 54 44"><path d="M27 2C13 2 2 9 2 19s11 17 25 17c2 0 4 0 6-1l12 8-3-11c6-3 10-8 10-13C52 9 41 2 27 2z" fill="#fff"/><circle cx="19" cy="19" r="5" fill="var(--teal-bottom)"/><circle cx="35" cy="19" r="5" fill="var(--teal-bottom)"/></svg>
      <span>Messages</span>
    </div>
    <div class="nav-item" style="width:220px;">
      <svg width="46" height="46" viewBox="0 0 46 46"><g fill="#fff"><circle cx="23" cy="23" r="15"/><rect x="19" y="1" width="8" height="44" rx="1"/><rect x="19" y="1" width="8" height="44" rx="1" transform="rotate(45 23 23)"/><rect x="19" y="1" width="8" height="44" rx="1" transform="rotate(90 23 23)"/><rect x="19" y="1" width="8" height="44" rx="1" transform="rotate(135 23 23)"/></g><circle cx="23" cy="23" r="7" fill="var(--teal-bottom)"/></svg>
      <span>Settings</span>
    </div>
  </footer>
</main>
</body>
</html>
```